Text only wordpress site to capture emails

Refer to inspiration upload for list of sites that will be useful for you.

We need a site that will be used to capture emails from clients that follow us on social media. The site will be all text, pretty simple. I have a couple of text sites that I like and we can use them for an example.

Menu section will have home, archive, about.
Footer will have © and Website Privacy Policy | Legal and Policies
There will be some text on the home page and an email capture.

This site will be all text no pictures.

I discuss office politics so the text portions will have some questions and answers on this and then prompt for the visitor to subscribe to my email list.

The only purpose of the site is to build an email list from existing social media followers so the site will be pretty simple in and of itself.

• Text only, similar Q&A to uploaded pics.

I will use a template from letter pinecone dotcom for email capture.

I like the simple couriernew font family that is on both sites supplied in the uploads.
• If you use any color it needs to be very minimal.

```html
<!DOCTYPE html>
<html lang="en">
<head>
<meta charset="utf-8">
<title>Brisk quill</title>
<link href="https://fonts.googleapis.com/css2?family=Courier+Prime:wght@400;700&display=swap" rel="stylesheet">
<style>
  :root {
    --backdrop: #777777;
    --paper: #ffffff;
    --ink: #111111;
    --ink-soft: #3a3a3a;
    --muted: #9a9a9a;
    --rule: #e6e6e6;
    --button: #222222;
    --button-text: #d8d8d8;
  }
  * { margin: 0; padding: 0; box-sizing: border-box; }
  html, body {
    width: 1200px; height: 870px; overflow: hidden;
    background: var(--backdrop);
    font-family: "Courier Prime", "Courier New", monospace;
    color: var(--ink-soft);
  }
  .page {
    position: absolute; left: 107px; top: 86px;
    width: 986px; height: 698px;
    background: var(--paper);
  }
  .site-header { position: absolute; left: 65px; top: 20px; width: 856px; height: 38px; border-bottom: 1px solid var(--rule); }
  .site-title { position: absolute; left: 0; top: 0; font-size: 20px; line-height: 20px; font-weight: 700; color: var(--ink); letter-spacing: 0.5px; }
  .main-nav a { position: absolute; top: 7px; font-size: 11px; line-height: 14px; color: var(--ink-soft); text-decoration: none; }
  .nav-home { left: 638px; }
  .nav-archive { left: 717px; top: 8px !important; }
  .nav-about { left: 823px; }

  .intro { position: absolute; left: 62px; top: 107px; width: 404px; }
  .intro-title { font-size: 12.3px; line-height: 20px; font-weight: 700; color: var(--ink); margin-bottom: 22px; white-space: nowrap; }
  .faq-item { margin-bottom: 17px; font-size: 9.4px; line-height: 17px; }
  .faq-q { font-weight: 700; color: var(--ink); }
  .faq-a { color: var(--ink-soft); }

  .signup { position: absolute; left: 626px; top: 118px; width: 300px; }
  .signup-title { width: 260px; font-size: 14px; line-height: 17.5px; letter-spacing: 1px; color: var(--ink-soft); font-weight: 400; }
  .signup-form { position: absolute; left: 0; top: 70px; width: 289px; height: 27px; }
  .email-field {
    position: absolute; left: 0; top: 0; width: 230px; height: 27px;
    border: 1px solid var(--rule); border-right: none;
    font-family: inherit; font-size: 8px; color: var(--muted);
    padding-left: 10px; background: var(--paper);
  }
  .email-field::placeholder { color: var(--muted); }
  .subscribe-button {
    position: absolute; left: 208px; top: 0; width: 81px; height: 27px;
    border: none; border-radius: 14px; background: var(--button);
    color: var(--button-text); font-family: inherit; font-size: 8px; letter-spacing: 0.3px;
  }
  .signup-note { position: absolute; left: 0; top: 115px; width: 300px; font-size: 11px; line-height: 14.5px; letter-spacing: 0.5px; color: var(--ink-soft); }

  .site-footer { position: absolute; left: 62px; top: 626px; width: 859px; font-size: 9.4px; line-height: 14px; color: var(--ink-soft); }
  .footer-links { position: absolute; right: 0; top: 0; }
  .footer-links a { color: var(--ink-soft); text-decoration: none; }
</style>
</head>
<body>
<div class="page">
  <header class="site-header">
    <div class="site-title">Brisk quill</div>
    <nav class="main-nav">
      <a class="nav-home" href="#">Home</a>
      <a class="nav-archive" href="#">Archive</a>
      <a class="nav-about" href="#">About</a>
    </nav>
  </header>

  <main class="intro">
    <h1 class="intro-title">The brisk quill is a market newsletter<br>for professional investors.</h1>
    <div class="faq-item">
      <p class="faq-q">Q: why a newsletter?</p>
      <p class="faq-a">A: the stuff that's out there right now isn't very good. there are very few people that can write well in this business. did you know that i won several spelling bees growing up?</p>
    </div>
    <div class="faq-item">
      <p class="faq-q">Q: really!</p>
      <p class="faq-a">A: yup. but beyond that, there's stuff that's too literary, stuff that assumes you'll listen to every idea, and stuff that manages to get the direction right, but not the timing.</p>
    </div>
    <div class="faq-item">
      <p class="faq-q">Q: yours is better?</p>
      <p class="faq-a">A: mine is better. my goal is to make my commentary a joy to read, in addition to being super-smart and timely as hell.</p>
    </div>
    <div class="faq-item">
      <p class="faq-q">Q: how are you qualified?</p>
      <p class="faq-a">A: i was a trader for eight years; four of which as an ETF trader.</p>
    </div>
    <div class="faq-item">
      <p class="faq-q">Q: you weren't just a flow monkey?</p>
      <p class="faq-a">A: absolutely not.</p>
    </div>
    <div class="faq-item">
      <p class="faq-q">Q: how much are subscriptions?</p>
      <p class="faq-a">A: $795/year. a firm may purchase a site license. you can learn more<br>here.</p>
    </div>
  </main>

  <aside class="signup">
    <h2 class="signup-title">The Latest Trends In Your Inbox Every Week.</h2>
    <form class="signup-form">
      <input class="email-field" type="email" placeholder="Your Email">
      <button class="subscribe-button" type="button">Subscribe</button>
    </form>
    <p class="signup-note">Join the brisk quill newsletterfor all updates in one place.</p>
  </aside>

  <footer class="site-footer">
    <span>©2021 Brisk quill</span>
    <span class="footer-links"><a href="#">Website Privacy Policy</a> | <a href="#">Legal and Policies</a></span>
  </footer>
</div>
</body>
</html>
```